Credit card acceptance poster

I need a poster explaining to my customers that the washers and dryers at my laundromat accept credit card payments and most mobile wallet payments. I have attached a flyer I made. It looks terrible so I need help. The cc readers accept: ZELO, TRUVENBANK, ORBINTAL, COLDRIDGE FUNDCO, KIVRA TAP, TREVO WAVE, AND ODELIX SWIPE.

Colors
0054AA
0677BA
7BADD7
CADEEF
E8F1F8

```html
<!DOCTYPE html>
<html lang="en">
<head>
<meta charset="utf-8">
<title>Sudswell Laundromat – Card Payments Poster</title>
<link href="https://fonts.googleapis.com/css2?family=Montserrat:wght@700;800;900&display=swap" rel="stylesheet">
<style>
  :root{
    --brand-deep:#0054AA;
    --brand-blue:#0677BA;
    --band-blue:#1779BE;
    --sky:#7BADD7;
    --mist:#CADEEF;
    --ice:#E8F1F8;
    --ink:#0b0b0b;
    --accent-yellow:#FFE81A;
    --white:#ffffff;
    --bubble-light:#f4f5f7;
    --bubble-mid:#dfe1e5;
  }
  *{margin:0;padding:0;box-sizing:border-box}
  html,body{width:764px;height:1200px;overflow:hidden;background:var(--white)}
  .poster{
    position:relative;width:764px;height:1200px;overflow:hidden;
    font-family:'Montserrat',Arial,sans-serif;
    background:radial-gradient(circle at 30% 20%,var(--bubble-light),var(--bubble-mid) 90%);
  }
  .bubbles-bg{position:absolute;inset:0}
  .brand{
    position:absolute;top:62px;left:0;right:0;
    display:flex;align-items:center;justify-content:center;gap:10px;
  }
  .brand-dot{width:34px;height:34px;border-radius:50%;background:var(--brand-blue)}
  .brand-name{
    font-weight:800;font-size:22px;letter-spacing:.5px;color:var(--brand-blue);line-height:1;
  }
  .headline{
    position:absolute;top:168px;left:0;right:0;text-align:center;
    font-weight:900;font-size:70px;line-height:80px;color:var(--ink);letter-spacing:-1px;
  }
  .hero-photo{
    position:absolute;left:0;top:360px;width:764px;height:540px;
  }
  .blue-band{position:absolute;left:0;top:860px;width:764px;height:340px}
  .accept-title{
    position:absolute;top:936px;left:0;right:0;text-align:center;
    font-weight:800;font-size:27px;color:var(--accent-yellow);letter-spacing:.2px;
  }
  .methods{
    position:absolute;top:1000px;left:0;right:0;
    display:flex;justify-content:center;gap:90px;
  }
  .method{display:flex;align-items:center;gap:14px}
  .method-icon{
    width:46px;height:46px;border-radius:50%;border:3px solid var(--accent-yellow);
    display:flex;align-items:center;justify-content:center;
  }
  .method-label{
    font-weight:700;font-size:14.5px;line-height:19px;color:var(--white);letter-spacing:.4px;
  }
  .acceptors{
    position:absolute;top:1100px;left:0;right:0;
    display:flex;justify-content:center;gap:5px;
  }
  .acceptor{
    width:96px;height:40px;background:var(--white);border-radius:3px;
    display:flex;align-items:center;justify-content:center;text-align:center;
    font-weight:800;font-size:10px;line-height:11px;color:var(--brand-deep);padding:0 4px;
  }
  .acceptor.dark{background:var(--brand-deep);color:var(--white)}
</style>
</head>
<body>
<main class="poster">
  <svg class="bubbles-bg" width="764" height="1200" role="img" aria-label="Soft white soap bubbles background">
    <circle cx="120" cy="90" r="70" fill="#ffffff" opacity=".45"/>
    <circle cx="640" cy="60" r="90" fill="#ffffff" opacity=".4"/>
    <circle cx="60" cy="380" r="80" fill="#ffffff" opacity=".4"/>
    <circle cx="700" cy="420" r="70" fill="#ffffff" opacity=".4"/>
    <circle cx="380" cy="30" r="50" fill="#ffffff" opacity=".35"/>
  </svg>

  <header class="brand">
    <span class="brand-dot"></span>
    <span class="brand-name">SUDSWELL LAUNDROMAT</span>
  </header>

  <h1 class="headline">NO CASH?<br>NO WORRIES!</h1>

  <svg class="hero-photo" width="764" height="540" role="img" aria-label="Photo collage: thoughtful man holding a laundry basket, a front-loading washer with water splash, folded shirts, iron, card payment reader, smartphone and credit card">
    <defs>
      <linearGradient id="heroFill" x1="0" y1="0" x2="1" y2="1">
        <stop offset="0" stop-color="#CADEEF"/>
        <stop offset=".5" stop-color="#b9bec6"/>
        <stop offset="1" stop-color="#7BADD7"/>
      </linearGradient>
    </defs>
    <rect x="40" y="0" width="680" height="540" rx="14" fill="url(#heroFill)" opacity=".85"/>
  </svg>

  <svg class="blue-band" width="764" height="340" viewBox="0 0 764 340" aria-hidden="true">
    <path d="M0 30 L40 18 L70 34 L110 22 L150 40 L200 28 L250 44 L300 30 L360 46 L420 32 L480 44 L540 26 L590 40 L640 22 L690 36 L730 18 L764 26 L764 340 L0 340 Z" fill="var(--white)"/>
    <path d="M0 46 L40 34 L72 50 L112 38 L152 56 L202 44 L252 60 L302 46 L362 62 L422 48 L482 60 L542 42 L592 56 L642 38 L692 52 L732 34 L764 42 L764 340 L0 340 Z" fill="var(--band-blue)"/>
  </svg>

  <h2 class="accept-title">OUR MACHINES NOW ACCEPT</h2>

  <section class="methods">
    <div class="method">
      <span class="method-icon">
        <svg width="26" height="20" viewBox="0 0 26 20" aria-hidden="true">
          <rect x="1" y="1" width="24" height="17" rx="2" fill="none" stroke="#fff" stroke-width="2"/>
          <rect x="1" y="5" width="24" height="3" fill="#fff"/>
          <rect x="4" y="12" width="7" height="3" fill="#fff"/>
        </svg>
      </span>
      <span class="method-label">CREDIT<br>CARDS</span>
    </div>
    <div class="method">
      <span class="method-icon">
        <svg width="18" height="26" viewBox="0 0 18 26" aria-hidden="true">
          <rect x="1" y="1" width="16" height="24" rx="3" fill="none" stroke="#fff" stroke-width="2"/>
          <text x="9" y="17" text-anchor="middle" font-family="Montserrat,Arial,sans-serif" font-weight="800" font-size="11" fill="#fff">$</text>
        </svg>
      </span>
      <span class="method-label">MOBILE<br>WALLET APPS</span>
    </div>
  </section>

  <section class="acceptors">
    <span class="acceptor">ZELO</span>
    <span class="acceptor">TRUVENBANK</span>
    <span class="acceptor">ORBINTAL</span>
    <span class="acceptor dark">COLDRIDGE FUNDCO</span>
    <span class="acceptor">KIVRA TAP</span>
    <span class="acceptor">TREVO WAVE</span>
    <span class="acceptor dark">ODELIX SWIPE</span>
  </section>
</main>
</body>
</html>
```